Business Cards for new orthopaedic surgery practice

My husband and I are starting our own orthopaedic surgery practice. We are looking for a business card that is uniform, but one will have my name/title and the other will have his. You can just create one design with my name on it for now. But when I choose your design as the winning design I will ask that you add another copy with his name/title.

We are looking for classy, simple, elite all in one. We like dark blues/a little gold/yellow. Something that goes with our logo. We want our logo incorporated. Here is all the info you need:
Business name: RV Spine & Vitality Center
Location: 38915 North Bramble Ave
Coral Springs, FL 33071
Phone: 954-218-4630
Fax: 954-571-2846
Email: info@myrvspine.example

Names: Lucinda Ferrow, M.D.
Board Certified Hand and Upper Extremity Surgeon

Emeka Dlunga, M.D.
Board Certified Hip & Knee Replacement/General Orthopaedic Surgeon

Can decide what you want to put on the back. Maybe a slogan:
Rooted in Care. Focused on You

I am just going to upload our logo. The only thing is if we select you as the winning design, the location, and phone numbers may change. We will need your help to update that once fully solidified.

Industry/Entity Type

Medical

Contact Information for Business Card

Colors
0054AA
0677BA
7BADD7
CADEEF
E8F1F8
0094D4
00A9DD
6FCCEA
C7EBF8
E9F6FB

Requirements
Must have
• class, appeal,
Should not have
• We want to air on the side of masculine if we are looking at masculine vs. feminine feel. But we still want it classy, sophisticated, and something we will love

```html
<!DOCTYPE html>
<html lang="en">
<head>
<meta charset="utf-8">
<title>RV Spine &amp; Vitality Center — Business Card</title>
<link rel="stylesheet" href="https://fonts.googleapis.com/css2?family=Fraunces:opsz,wght@9..144,800&family=Inter:wght@400;500&display=swap">
<style>
  :root {
    --backdrop: #6b5c42;
    --card: #efe4d3;
    --navy: #15265e;
    --gold: #c9a45c;
    --gold-soft: #e3cfa6;
  }
  * { margin: 0; padding: 0; box-sizing: border-box; }
  html, body { width: 1200px; height: 800px; overflow: hidden; }
  body { background: var(--backdrop); position: relative; font-family: "Inter", sans-serif; color: var(--navy); }

  .card {
    position: absolute; left: 383px; width: 435px; height: 248px;
    background: var(--card);
    box-shadow: 6px 10px 18px rgba(0,0,0,.25);
    overflow: hidden;
  }
  .card--front { top: 122px; }
  .card--back { top: 430px; }

  .front-texture {
    position: absolute; inset: 0;
    background: radial-gradient(circle at 50% 50%, var(--card) 0 30%, #ead9bc 31% 33%, var(--card) 34% 55%, #e8d6b6 70%, var(--card) 100%);
  }
  .brand-name {
    position: absolute; left: 0; right: 0; top: 50%; transform: translateY(-50%);
    text-align: center;
    font-family: "Fraunces", serif; font-weight: 800;
    font-size: 25px; line-height: 1.15; color: var(--navy);
  }

  .doctor-name {
    position: absolute; right: 25px; top: 16px;
    text-align: right;
    font-family: "Fraunces", serif; font-weight: 800;
    font-size: 37px; line-height: 36px; letter-spacing: -0.5px;
  }
  .credential {
    position: absolute; right: 25px; top: 98px;
    display: flex; align-items: center; gap: 6px;
    font-family: "Fraunces", serif; font-weight: 800; font-size: 11px; color: #2f5a8a;
  }
  .credential::before {
    content: ""; width: 38px; height: 2px; background: var(--gold);
  }

  .contact-list { position: absolute; left: 24px; top: 112px; list-style: none; }
  .contact-item {
    display: flex; align-items: center; gap: 10px;
    font-size: 13.5px; line-height: 14px; margin-bottom: 14px;
  }
  .contact-item:first-child { align-items: flex-start; }
  .contact-icon { width: 15px; height: 15px; flex: none; fill: var(--navy); }

  .specialty {
    position: absolute; right: 17px; top: 184px;
    display: flex; align-items: center; gap: 9px;
    text-align: right; font-size: 13.5px; line-height: 14px;
  }
  .specialty-bars { display: flex; flex-direction: column; gap: 3px; }
  .specialty-bars span { width: 4px; height: 10px; background: var(--gold); }
</style>
</head>
<body>
  <section class="card card--front">
    <div class="front-texture" role="img" aria-label="Gold fine-line lattice with concentric circles on cream"></div>
    <p class="brand-name">RV Spine &amp;<br>Vitality Center</p>
  </section>

  <section class="card card--back">
    <h1 class="doctor-name">Lucinda<br>Ferrow</h1>
    <p class="credential">M.D.</p>

    <ul class="contact-list">
      <li class="contact-item">
        <svg class="contact-icon" viewBox="0 0 24 24"><path d="M12 1a8 8 0 0 0-8 8c0 6 8 14 8 14s8-8 8-14a8 8 0 0 0-8-8zm0 11a3 3 0 1 1 0-6 3 3 0 0 1 0 6z"/></svg>
        <span>38915 North Bramble Ave<br>Coral Springs, FL 33071</span>
      </li>
      <li class="contact-item">
        <svg class="contact-icon" viewBox="0 0 24 24"><path d="M6.6 10.8a15 15 0 0 0 6.6 6.6l2.2-2.2a1 1 0 0 1 1-.25 11 11 0 0 0 3.6.6 1 1 0 0 1 1 1V20a1 1 0 0 1-1 1A17 17 0 0 1 3 4a1 1 0 0 1 1-1h3.5a1 1 0 0 1 1 1c0 1.25.2 2.45.6 3.6a1 1 0 0 1-.25 1z"/></svg>
        <span>954-218-4630</span>
      </li>
      <li class="contact-item">
        <svg class="contact-icon" viewBox="0 0 24 24"><path d="M2 6h4v16H2zM8 3h9l3 3v16H8zm3 8v2h2v-2zm4 0v2h2v-2zm-4 4v2h2v-2zm4 0v2h2v-2zM10 5v4h8V6.5L16.5 5z"/></svg>
        <span>954-571-2846</span>
      </li>
      <li class="contact-item">
        <svg class="contact-icon" viewBox="0 0 24 24"><path d="M2 4h20v16H2zm2 2.5V8l8 5 8-5V6.5l-8 5z"/></svg>
        <span>info@myrvspine.example</span>
      </li>
    </ul>

    <div class="specialty">
      <p>Board Certified Hand &amp;<br>Upper Extremity Surgeon</p>
      <div class="specialty-bars"><span></span><span></span><span></span></div>
    </div>
  </section>
</body>
</html>
```